Delivery Docket urgent plus require many other designs for more stationary after this.

We need a new delivery docket design urgently as the one we have needs updating and we have changed our company name. Please do not copy the one I have uploaded as we do not feel this looks professional enough. I uploaded it as a few designers requested to see what we are currently using thank you.
It is quite complex in that we need a range of information to be on the one docket.
We are a Transport Company based in Australia that has a wide variety of items that we deliver such as water, sand and gravels and heavy equipment transport.
We would prefer to keep this design to A5 size as we will get them made into books. We are looking for a modern professional look. Although it is only a delivery docket this is given to all our customers so needs to look impressive.

We need our new logo on the docket (Tallowby). There will also need to be areas for our address and contact numbers, email etc these will be supplied to the winning designer to make the final adjustments so for now just put something generic in these spaces.
Needs to have an area for customer details, purchase order number, date and docket number (docket number to be in red)
Needs a section where we can list the type of product / and or service that has been provided and the amount / qty usually 3 lines will be enough for this. Need area under this where the customer can sign name and print name to say that the goods / and or services have been received.

Also required somewhere on the docket are the words, Tax Invoice will be issued based on the information provided on this docket. Conditions on back of page

We then need a separate section on the same page which we will use internally that the staff member can tear off and hand into the office. On this section it needs to have area where the driver can list km at start of job and at end with space to calculate km travelled, details of fuel purchased eg amount and litres, vehicle that is being used. also need to log down wheel bearing temps.
prime mover needs spaces as follows
Steer axel FL____________ Steer axel FR _________ 1st drive axel L_______
1st drive axel R_________ 2nd drive axel L_______ 2nd drive axel R________

For the trailers need something similar x 2 as have 2 trailers
1st axel DS_________ 1st axel PS_________ 2nd axel DS__________
2nd axel PS_________ 3rd axel DS_________ 3rd axel PS__________

I have included a few examples of designs we have used in past and ones that we like so you can get an idea of the colours we prefer, I have included some of the designs we are currently receiving for our logo that I like so you can get idea again of colours we prefer. There is much more we need designed also such as time sheets, more delivery dockets and letter heads so there is a lot of more work available to the winning designer.

Thank you

Target Market(s)

Customers

Font styles to use
Serif
Sans Serif

Colors

Designer to choose colors to be used in the design.

Requirements
Should not have
• Please don't copy old docket as we do not like it and nned new info on new design thank you

```html
<!DOCTYPE html>
<html lang="en">
<head>
<meta charset="utf-8">
<title>Tallowby Delivery Docket</title>
<link rel="stylesheet" href="https://fonts.googleapis.com/css2?family=Arimo:wght@400;700&family=Roboto+Condensed:wght@700&display=swap">
<style>
:root{
  --stage:#e8e8e8;
  --frame-blue:#a9c3d6;
  --panel:#dce6ed;
  --head:#7f97a8;
  --line:#6f8494;
  --ink:#2b2b2b;
  --red:#d7141a;
  --paper:#ffffff;
  --band:#ccd7de;
  --page-frame:#8c8c8c;
  --label-bg:#e6e9ec;
  --note-band:#9aa9b4;
}
*{box-sizing:border-box;margin:0;padding:0}
html,body{width:1200px;height:525px;overflow:hidden;background:var(--stage)}
body{position:relative;font-family:"Arimo",Arial,sans-serif;color:var(--ink)}

.docket{position:absolute;left:37px;top:57px;width:543px;height:407px;background:var(--frame-blue);padding:7px}
.docket-inner{position:relative;width:100%;height:100%;background:var(--panel)}
.docket-inner>*{position:absolute}

.brand-mark{left:13px;top:8px;width:86px;height:47px;background:var(--paper);border:1px solid #333;display:flex;align-items:center;justify-content:center;gap:5px}
.brand-mark .sq{width:8px;height:8px;background:var(--ink);flex:none}
.brand-mark .name{font-weight:700;font-size:13px;color:var(--ink);white-space:nowrap}
.business{left:107px;top:15px;font-size:10.5px;line-height:15px;font-weight:700}
.business .depot{font-weight:400}
.address{left:19px;top:69px;font-size:10px;line-height:15px}
.address b{font-weight:700}

.customer{left:266px;top:8px;width:246px;height:125px;border:1px solid #444;border-radius:7px;overflow:hidden;background:var(--paper)}
.customer .row{position:absolute;left:0;width:100%;height:25px;border-bottom:1px solid #444}
.customer .row:last-child{border-bottom:none}
.customer .cell{position:absolute;top:0;height:100%;font-size:8.5px;padding:3px 3px}
.customer .cell.left{left:0;width:124px;border-right:1px solid #444}
.customer .cell.right{left:124px;right:0}
.customer .cell.full{left:0;right:0}
.customer .title{background:var(--head);font-size:10.5px;font-weight:700;color:#1e1e1e;display:flex;align-items:center;justify-content:center}
.customer .docket-no{font-size:9.5px;font-weight:700;display:flex;align-items:center;gap:5px;padding:0 0 0 4px;white-space:nowrap}
.customer .docket-no span{font-family:"Roboto Condensed","Arial Narrow",sans-serif;color:var(--red);font-size:16px}
.field-label{background:var(--label-bg);padding:0 2px}

.grid{border-collapse:collapse;background:var(--paper);font-size:8.5px}
.grid th{background:var(--head);color:#fff;font-weight:700;border:1px solid var(--line);padding:0;text-align:center}
.grid td{border:1px solid var(--line)}
.items{left:16px;top:134px;width:497px}
.items th{height:19px}.items td{height:19px}
.received{left:16px;top:214px;width:497px}
.received th{height:16px}.received td{height:17px}
.travel{left:16px;top:284px;width:497px}
.travel th{height:16px}.travel td{height:19px}

.bearings{left:19px;top:321px;width:300px;font-size:7.2px;color:#444}
.bearings p{height:14px;line-height:14px;white-space:nowrap}
.bearings .trailer-note{background:var(--note-band);color:#333;margin-left:-2px;padding-left:2px;width:288px}

.tax-note{left:311px;top:327px;width:199px;height:50px;background:var(--paper);border:1px solid #cfd6db;font-size:9.5px;line-height:12px;text-align:center;display:flex;align-items:center;justify-content:center;color:#333}

.terms-page{position:absolute;left:593px;top:57px;width:542px;height:407px;background:var(--paper)}
.terms-frame{position:absolute;left:25px;top:19px;width:492px;height:369px;border:1px solid var(--page-frame)}
.terms-title{position:absolute;left:45px;top:61px;width:402px;height:19px;background:var(--band);font-size:11.5px;font-weight:700;text-align:center;line-height:19px;color:#333}
.terms-text{position:absolute;left:47px;top:91px;font-size:8.5px;color:#333}
.terms-text p{height:18.5px;white-space:nowrap}
</style>
</head>
<body>

<section class="docket">
  <div class="docket-inner">
    <div class="brand-mark"><span class="sq"></span><span class="name">Tallowby</span></div>
    <div class="business">Business Name<br>ABN:<br><span class="depot">Depot:</span></div>
    <div class="address">Street Address<br>Town<br><b>Ph: 000 000 0000</b><br>Email:info@........com</div>

    <div class="customer">
      <div class="row" style="top:0;height:26px">
        <div class="cell left title">Customer Details</div>
        <div class="cell right docket-no">Delivery Docket <span>2050</span></div>
      </div>
      <div class="row" style="top:26px"><div class="cell left"><span class="field-label">Name:</span></div><div class="cell right"><span class="field-label">Date:</span></div></div>
      <div class="row" style="top:51px"><div class="cell left"><span class="field-label">Order Number:</span></div><div class="cell right"></div></div>
      <div class="row" style="top:76px"><div class="cell left"><span class="field-label">Contact:</span></div><div class="cell right"><span class="field-label">Phone:</span></div></div>
      <div class="row" style="top:101px;height:24px"><div class="cell full"><span class="field-label">Billing Address:</span></div></div>
    </div>

    <table class="grid items">
      <tr><th style="width:96px">Qty</th><th>Description</th></tr>
      <tr><td></td><td></td></tr>
      <tr><td></td><td></td></tr>
      <tr><td></td><td></td></tr>
    </table>

    <table class="grid received">
      <tr><th style="width:257px">Good Received by (Print Name)</th><th style="width:70px">QTY</th><th style="width:71px">AMOUNT</th><th>SIGNED</th></tr>
      <tr><td></td><td></td><td></td><td></td></tr>
      <tr><td></td><td></td><td></td><td></td></tr>
      <tr><td></td><td></td><td></td><td></td></tr>
    </table>

    <table class="grid travel">
      <tr><th style="width:97px">Start Km</th><th style="width:108px">Calculate km travelled</th><th style="width:122px">Details of fuel purchased</th><th style="width:71px">Litres</th><th>Amount</th></tr>
      <tr><td></td><td></td><td></td><td></td><td></td></tr>
    </table>

    <div class="bearings">
      <p>Steer axel FL_____________ Steer axel FR _________ 1st drive axel L________</p>
      <p>&nbsp;1st drive axel R_________ 2nd drive axel L_______ 2nd drive axel R________</p>
      <p class="trailer-note">For the trailers need something similar x 2 as have 2 trailers</p>
      <p>&nbsp;1st axel DS_________ 1st axel PS_________ 2nd axel DS__________</p>
      <p>&nbsp;2nd axel PS_________ 3rd axel DS_________ 3rd axel PS__________</p>
    </div>

    <div class="tax-note">Tax Invoice will be issued based on the information provided on this docket.<br>Conditions on back of page</div>
  </div>
</section>

<section class="terms-page">
  <div class="terms-frame">
    <h2 class="terms-title">TERMS &amp; CONDITIONS</h2>
    <div class="terms-text">
      <p>I have included a few examples of designs we have used in</p>
      <p>&nbsp;past and ones that we like so you can get an idea of the colours we prefer.</p>
      <p>I have included some of the designs we are currently receiving for our logo</p>
      <p>that I like so you can get idea again of colours we prefer. There is much</p>
      <p>more we need designed also such as time sheets, more delivery dockets</p>
      <p>&nbsp;and letter heads so there is a lot of more work available to the winning designer</p>
      <p>I have included a few examples of designs we have used in</p>
      <p>&nbsp;past and ones that we like so you can get an idea of the colours we prefer.</p>
      <p>I have included some of the designs we are currently receiving for our logo</p>
      <p>that I like so you can get idea again of colours we prefer. There is much</p>
      <p>more we need designed also such as time sheets, more delivery dockets</p>
      <p>&nbsp;and letter heads so there is a lot of more work available to the winning designer</p>
    </div>
  </div>
</section>

</body>
</html>
```